Home change of address

Martin & Priya Colwell
WE HAVE MOVED
The address of our new home is
Birch Hollow
47 Thornbury Lane Road
Ashcombe on Wend
Warwickshire
B72 8QT
Tel: 07912 384071
Email: martin@pelmora.uk.com

```html
<!DOCTYPE html>
<html lang="en">
<head>
<meta charset="utf-8">
<title>Martin &amp; Priya Colwell – We have moved</title>
<link rel="stylesheet" href="https://fonts.googleapis.com/css2?family=Didact+Gothic&family=Sniglet:wght@400;800&family=Mali:wght@500&display=swap">
<style>
  :root {
    --cream: #f6e6c7;
    --navy: #1f2142;
    --red: #e84848;
    --white: #ffffff;
  }
  * { margin: 0; padding: 0; box-sizing: border-box; }
  html, body { width: 970px; height: 1200px; overflow: hidden; background: var(--cream); }
  .card {
    position: relative;
    width: 970px;
    height: 1200px;
    background: var(--cream);
    color: var(--navy);
    overflow: hidden;
  }
  .couple {
    position: absolute;
    left: 158px;
    top: 96px;
    font-family: "Didact Gothic", sans-serif;
    font-size: 64px;
    letter-spacing: -1px;
    white-space: nowrap;
  }
  .couple .amp { color: var(--red); font-family: "Mali", cursive; }
  .headline {
    position: absolute;
    font-family: "Sniglet", cursive;
    font-weight: 400;
    line-height: 1;
    white-space: nowrap;
  }
  .headline-top { left: 74px; top: 244px; font-size: 118px; }
  .headline-bottom { left: 256px; top: 340px; font-size: 108px; }
  .address {
    position: absolute;
    left: 62px;
    top: 536px;
    font-family: "Mali", cursive;
    font-weight: 500;
    font-size: 35px;
    line-height: 1.1;
  }
  .address .intro { margin-bottom: 20px; }
  .address .line { margin-bottom: 26px; }
  .strings { position: absolute; inset: 0; }
  .hanging {
    position: absolute;
  }
  .hanging-tree { left: 399px; top: 816px; width: 138px; height: 244px; background: var(--red); border-radius: 60px 60px 6px 6px; }
  .hanging-house { left: 515px; top: 650px; width: 256px; height: 300px; background: linear-gradient(var(--red) 0 32%, var(--white) 32% 100%); border-radius: 6px; }
  .hanging-cat-large { left: 804px; top: 732px; width: 132px; height: 196px; background: var(--white); border-radius: 40px 40px 20px 20px; }
  .hanging-cat-small { left: 740px; top: 858px; width: 106px; height: 160px; background: var(--white); border-radius: 34px 34px 18px 18px; }
  .contact-bar {
    position: absolute;
    left: 0;
    top: 1112px;
    width: 970px;
    height: 88px;
    background: var(--navy);
    color: var(--cream);
    font-family: "Mali", cursive;
    font-weight: 500;
    font-size: 33px;
  }
  .contact {
    position: absolute;
    top: 20px;
    display: flex;
    align-items: center;
    gap: 10px;
    white-space: nowrap;
  }
  .contact-phone { left: 76px; }
  .contact-email { left: 455px; }
  .contact svg { fill: var(--cream); }
</style>
</head>
<body>
<main class="card">
  <svg class="strings" width="970" height="1200" viewBox="0 0 970 1200" aria-hidden="true">
    <line x1="636" y1="170" x2="636" y2="690" stroke="#1f2142" stroke-width="6"/>
    <line x1="461" y1="428" x2="461" y2="822" stroke="#ffffff" stroke-width="5"/>
    <line x1="793" y1="0" x2="793" y2="870" stroke="#e84848" stroke-width="6"/>
    <line x1="875" y1="0" x2="875" y2="752" stroke="#e84848" stroke-width="6"/>
  </svg>

  <h1 class="couple">Martin <span class="amp">&amp;</span> Priya Colwell</h1>

  <h2 class="headline headline-top">We have</h2>
  <h2 class="headline headline-bottom">moved</h2>

  <div class="hanging hanging-tree" role="img" aria-label="Hanging tag illustration of a red tree"></div>
  <div class="hanging hanging-house" role="img" aria-label="Hanging tag illustration of a white house with a red roof"></div>
  <div class="hanging hanging-cat-large" role="img" aria-label="Hanging tag illustration of a white cat"></div>
  <div class="hanging hanging-cat-small" role="img" aria-label="Hanging tag illustration of a small white kitten"></div>

  <address class="address">
    <p class="intro">The address of our<br>new home is:</p>
    <p class="line">Birch Hollow</p>
    <p class="line">47 Thornbury Lane Road</p>
    <p class="line">Ashcombe on Wend</p>
    <p class="line">Warwickshire</p>
    <p class="line">B72 8QT</p>
  </address>

  <footer class="contact-bar">
    <div class="contact contact-phone">
      <svg width="32" height="34" viewBox="0 0 24 24" aria-hidden="true"><path d="M6.6 10.8a15.1 15.1 0 0 0 6.6 6.6l2.2-2.2a1 1 0 0 1 1-.25 11.4 11.4 0 0 0 3.6.57 1 1 0 0 1 1 1V20a1 1 0 0 1-1 1A17 17 0 0 1 3 4a1 1 0 0 1 1-1h3.5a1 1 0 0 1 1 1c0 1.25.2 2.45.57 3.6a1 1 0 0 1-.25 1z"/></svg>
      <span>07912 384071</span>
    </div>
    <div class="contact contact-email">
      <svg width="34" height="24" viewBox="0 0 34 24" aria-hidden="true"><path d="M0 0h34v24H0z M3 3v1l14 10 14-10V3z M3 7v14h28V7L17 17z" fill-rule="evenodd"/></svg>
      <span>martin@pelmora.uk.com</span>
    </div>
  </footer>
</main>
</body>
</html>
```